International Development Cooperation Consultant needs a business card design

I need a business card design for myself as a way to present and introduce to wide range of organisations: international organisations, NGOs, governments, universities....
I am a consultant working in the field of governance, civil society and public sector. I carry out studies and provide advice for development agencies as well as think tanks on different topics such as civil society organisations in developing countries, corruption, climate change, monitoring and evaluation. I also provide technical assistance to governments in developing countries... These studies should help for example NGOs to play a better role in poor countries or where they are threatened, or improved the impact of aid in developing countries. Technical capacity should strengthen the organisation and empower the public civl servants in those countries. I would like to see designs that give a fresh, young, positive, alternative but at the same time serious impression. That reflects change, connecting people, the world, knowledge, multi-culturality... Most of people I have worked with say that 'I make things happen' !
Industry/Entity Type
Business
Contact Information for Business Card
Laia Bertran Soler
International Development Consultant
Governance Expert
E-mail: laiabertran@correuweb.example
Phone: +34628351470

```html
<!DOCTYPE html>
<html lang="en">
<head>
<meta charset="utf-8">
<title>Laia Bertran Soler – Business Card</title>
<link rel="stylesheet" href="https://fonts.googleapis.com/css2?family=Michroma&display=swap">
<style>
  :root {
    --backdrop: #a3a3a3;
    --card-grey: #d3d3d3;
    --card-white: #ffffff;
    --violet-dark: #9b4fa0;
    --violet-light: #c07cb8;
    --ink: #3a3a3a;
  }
  * { margin: 0; padding: 0; box-sizing: border-box; }
  html, body {
    width: 1200px; height: 800px; overflow: hidden;
    background: var(--backdrop);
    font-family: "Michroma", "Arial", sans-serif;
  }
  .canvas { position: relative; width: 1200px; height: 800px; }

  .card {
    position: absolute; top: 120px;
    width: 340px; height: 560px;
    border-radius: 22px; overflow: hidden;
  }

  /* Front */
  .card-front { left: 200px; background: var(--card-grey); }
  .front-stripe {
    position: absolute; left: 44px; top: 0; bottom: 0;
    width: 7px; background: var(--violet-light);
  }
  .front-brand {
    position: absolute; left: 80px; right: 24px; top: 70px;
    display: flex; align-items: center; gap: 10px;
    color: var(--violet-dark); font-size: 15px; line-height: 1.3;
  }
  .brand-square { width: 18px; height: 18px; background: var(--violet-dark); flex: none; }
  .front-rule {
    position: absolute; left: 66px; width: 238px; top: 200px;
    height: 2px; background: var(--violet-dark);
  }
  .contact-block {
    position: absolute; top: 218px; right: 70px;
    max-height: 320px;
    writing-mode: vertical-rl;
    font-variant: small-caps; color: var(--ink);
    font-size: 11px; line-height: 20px; letter-spacing: 0.3px;
    white-space: nowrap;
  }
  .contact-name { color: var(--violet-light); font-size: 18px; line-height: 28px; letter-spacing: 0.5px; }
  .contact-row { display: flex; align-items: center; gap: 8px; line-height: 24px; }
  .contact-email { font-size: 11px; }
  .contact-phone { font-size: 15px; line-height: 26px; }
  .contact-row svg { width: 12px; height: 12px; fill: var(--ink); flex: none; }

  /* Back */
  .card-back { left: 660px; background: var(--card-white); }
  .back-band {
    position: absolute; left: 0; top: 0; bottom: 0; width: 14px;
    display: flex; flex-direction: column;
  }
  .band-dark { background: var(--violet-dark); flex: 1; }
  .band-light { background: var(--violet-light); flex: 1; }
  .back-brand {
    position: absolute; inset: 0;
    display: flex; align-items: center; justify-content: center; gap: 14px;
    color: var(--violet-dark); font-size: 20px; line-height: 1.4;
  }
  .back-brand .brand-square { width: 26px; height: 26px; }
</style>
</head>
<body>
<main class="canvas">
  <section class="card card-front">
    <div class="front-stripe"></div>
    <div class="front-brand"><span class="brand-square"></span><span>Bertran Consulting</span></div>
    <div class="front-rule"></div>
    <div class="contact-block">
      <div class="contact-name">Laia Bertran Soler</div>
      <div>International Development Consultant</div>
      <div>Governance Expert</div>
      <div class="contact-row contact-email">
        <svg viewBox="0 0 16 16" aria-hidden="true"><path d="M1 3h14v10H1z M2 4v.5l6 4.5 6-4.5V4z" fill-rule="evenodd"/></svg>
        <span>laiabertran@correuweb.example</span>
      </div>
      <div class="contact-row contact-phone">
        <svg viewBox="0 0 16 16" aria-hidden="true"><path d="M4 1h3l1 4-2 1.5c.8 1.8 2 3 3.5 3.5L11 8l4 1v3c0 1-1 2-2 2C7 14 2 9 2 3c0-1 1-2 2-2z"/></svg>
        <span>+34628351470</span>
      </div>
    </div>
  </section>

  <section class="card card-back">
    <div class="back-band">
      <div class="band-dark"></div>
      <div class="band-light"></div>
      <div class="band-dark"></div>
      <div class="band-light"></div>
      <div class="band-dark"></div>
    </div>
    <div class="back-brand"><span class="brand-square"></span><span>Bertran<br>Consulting</span></div>
  </section>
</main>
</body>
</html>
```